Company Profile

Redesign of Business Profile for print in A4 format. The design pages should complete a booklet. Kindly use Pictures as well as projects from our website @kelmoritaestates.co.za

Target Market(s)

Business, Construction

```html
<!DOCTYPE html>
<html lang="en">
<head>
<meta charset="utf-8">
<title>Kelmorita Estates – Company Profile</title>
<link rel="stylesheet" href="https://fonts.googleapis.com/css2?family=Bebas+Neue&family=Montserrat:wght@400;500;600;700&display=swap">
<style>
  :root {
    --maroon: #7e2a1f;
    --maroon-deep: #6f241a;
    --charcoal: #414042;
    --white: #ffffff;
    --sky: #dcedf3;
    --canvas: #b5b5b5;
    --rule: #b9b9b9;
  }
  * { margin: 0; padding: 0; box-sizing: border-box; }
  html, body { width: 1200px; height: 2464px; overflow: hidden; }
  body { background: var(--canvas); font-family: "Montserrat", sans-serif; color: var(--white); position: relative; }

  .page { position: absolute; width: 522px; height: 738px; overflow: hidden; background: var(--maroon); }
  .page--cover { left: 49px; top: 862px; background: var(--white); }
  .page--copyright { left: 629px; top: 862px; }
  .page--services { left: 49px; top: 1648px; }
  .page--contents { left: 629px; top: 1648px; background: var(--sky); }

  .photo { position: absolute; display: block; }

  .brand { position: absolute; font-family: "Bebas Neue", sans-serif; color: var(--maroon); letter-spacing: 1px; line-height: 1; white-space: nowrap; }

  /* Cover */
  .cover-photo { left: 0; top: 0; width: 522px; height: 516px; background: linear-gradient(135deg, #d9eef4 0%, #c9b08c 45%, #9b6a4a 70%, #3f3f44 100%); }
  .cover-brand { right: 32px; top: 30px; font-size: 44px; }
  .cover-band { position: absolute; left: 0; top: 516px; width: 522px; height: 222px; }
  .cover-band svg { position: absolute; inset: 0; }
  .cover-title { position: absolute; left: 31px; top: 532px; font-family: "Bebas Neue", sans-serif; font-weight: 400; font-size: 35px; line-height: 36px; }
  .cover-list { position: absolute; left: 31px; top: 607px; font-weight: 700; font-size: 14px; line-height: 19px; text-transform: uppercase; }
  .cover-url { position: absolute; left: 31px; top: 706px; font-size: 14px; }
  .cover-square { position: absolute; right: 32px; top: 580px; width: 80px; height: 80px; background: var(--maroon); }

  /* Footer shared */
  .footer { position: absolute; left: 0; bottom: 0; width: 522px; height: 58px; }
  .footer svg { position: absolute; inset: 0; }
  .footer-tag { position: absolute; left: 31px; top: 14px; font-weight: 700; font-size: 11px; line-height: 15px; }
  .footer-url { position: absolute; left: 207px; top: 22px; font-size: 11px; }
  .footer-brand { right: 30px; top: 9px; font-size: 21px; line-height: 20px; text-align: right; }
  .page-number { position: absolute; width: 30px; height: 30px; background: var(--charcoal); font-size: 13px; text-align: center; line-height: 30px; }

  /* Copyright */
  .copyright-photo { inset: 0 0 58px 0; background: linear-gradient(180deg, #85301f 0%, #7a2a1e 60%, #6e271c 100%); }
  .seal { position: absolute; left: 139px; top: 132px; width: 244px; height: 244px; border-radius: 50%; background: var(--white); }
  .seal-name { left: 0; right: 0; top: 82px; text-align: center; font-size: 42px; line-height: 40px; }
  .copyright-text { position: absolute; left: 0; right: 0; top: 410px; text-align: center; font-weight: 600; font-size: 14px; line-height: 20px; }

  /* Services */
  .service-list { position: absolute; top: 30px; list-style: none; font-weight: 600; font-size: 15px; line-height: 30px; text-transform: uppercase; }
  .service-list--left { left: 31px; }
  .service-list--right { left: 277px; }
  .service-list li { display: flex; align-items: center; gap: 8px; }
  .service-list svg { width: 11px; height: 11px; flex: none; }
  .mission { position: absolute; left: 31px; top: 185px; width: 480px; font-size: 11px; line-height: 14.5px; text-transform: uppercase; }
  .services-photo { left: 0; top: 296px; width: 522px; height: 384px; background: linear-gradient(180deg, #1f2f7a 0%, #3a5f8a 35%, #6c6a4a 55%, #a35a44 72%, #bda79a 100%); }

  /* Contents */
  .contents-column { position: absolute; left: 0; top: 0; width: 262px; height: 680px; background: var(--maroon); }
  .contents-heading { position: absolute; left: 31px; top: 30px; font-size: 20px; line-height: 22px; font-weight: 500; }
  .contents-heading strong { display: block; font-size: 28px; line-height: 32px; font-weight: 700; }
  .quote-mark { position: absolute; font-family: "Bebas Neue", sans-serif; font-size: 60px; line-height: 1; }
  .quote-open { left: 31px; top: 168px; }
  .quote-close { left: 158px; top: 300px; }
  .contents-quote { position: absolute; left: 31px; top: 218px; font-family: "Bebas Neue", sans-serif; font-size: 31px; line-height: 32px; }
  .toc { position: absolute; left: 283px; top: 26px; width: 207px; list-style: none; color: #333; font-size: 10px; }
  .toc li { display: flex; justify-content: space-between; height: 26.3px; padding-top: 6px; border-bottom: 1px solid var(--rule); }
  .contents-photo { left: 0; top: 355px; width: 522px; height: 325px; background: linear-gradient(180deg, rgba(220,237,243,0) 0%, #8c8580 25%, #a85a40 55%, #6d6a6a 100%); }
</style>
</head>
<body>

<!-- Cover -->
<section class="page page--cover">
  <div class="photo cover-photo" role="img" aria-label="Upward view of a brick multi-storey office building with maroon fins against a pale sky"></div>
  <div class="brand cover-brand">KELMORITA ESTATES</div>
  <div class="cover-band">
    <svg width="522" height="222" viewBox="0 0 522 222">
      <polygon points="0,0 292,0 420,158 0,158" fill="var(--maroon)"/>
      <polygon points="0,158 420,158 470,222 0,222" fill="var(--charcoal)"/>
      <polygon points="300,0 312,0 500,222 488,222" fill="var(--charcoal)"/>
    </svg>
  </div>
  <div class="cover-square"></div>
  <h1 class="cover-title">Infrastructure<br>Provider of Distinction</h1>
  <p class="cover-list">Roads &amp; Civils Buildings<br>Water &amp; Sanitation Structures<br>Property Development Mining Services<br>Facilities Management</p>
  <p class="cover-url">www.kelmoritaestates.co.za</p>
</section>

<!-- Copyright page -->
<section class="page page--copyright">
  <div class="photo copyright-photo" role="img" aria-label="Faint maroon-toned building facade in the background"></div>
  <div class="seal"><div class="brand seal-name">KELMORITA<br>ESTATES</div></div>
  <p class="copyright-text">COPYRIGHT © 2021 | KELMORITA ESTATES<br>ALL RIGHT RESERVED.</p>
  <div class="page-number" style="left:31px; top:650px;">2</div>
  <footer class="footer">
    <svg width="522" height="58" viewBox="0 0 522 58">
      <rect width="522" height="58" fill="var(--charcoal)"/>
      <polygon points="370,0 522,0 522,58 420,58" fill="var(--white)"/>
    </svg>
    <p class="footer-tag">INFRASTRUCTURE<br>PROVIDER OF DISTINCTION</p>
    <p class="footer-url">www.kelmoritaestates.co.za</p>
    <div class="brand footer-brand">KELMORITA<br>ESTATES</div>
  </footer>
</section>

<!-- Services page -->
<section class="page page--services">
  <ul class="service-list service-list--left">
    <li><svg viewBox="0 0 12 12"><circle cx="6" cy="6" r="6" fill="#fff"/><path d="M3.2 6.2 5.2 8 8.8 4" stroke="var(--maroon)" stroke-width="1.6" fill="none"/></svg>Roads &amp; Civils</li>
    <li><svg viewBox="0 0 12 12"><circle cx="6" cy="6" r="6" fill="#fff"/><path d="M3.2 6.2 5.2 8 8.8 4" stroke="var(--maroon)" stroke-width="1.6" fill="none"/></svg>Buildings</li>
    <li><svg viewBox="0 0 12 12"><circle cx="6" cy="6" r="6" fill="#fff"/><path d="M3.2 6.2 5.2 8 8.8 4" stroke="var(--maroon)" stroke-width="1.6" fill="none"/></svg>Water &amp; Sanitation</li>
    <li><svg viewBox="0 0 12 12"><circle cx="6" cy="6" r="6" fill="#fff"/><path d="M3.2 6.2 5.2 8 8.8 4" stroke="var(--maroon)" stroke-width="1.6" fill="none"/></svg>Structures</li>
  </ul>
  <ul class="service-list service-list--right">
    <li><svg viewBox="0 0 12 12"><circle cx="6" cy="6" r="6" fill="#fff"/><path d="M3.2 6.2 5.2 8 8.8 4" stroke="var(--maroon)" stroke-width="1.6" fill="none"/></svg>Property Development</li>
    <li><svg viewBox="0 0 12 12"><circle cx="6" cy="6" r="6" fill="#fff"/><path d="M3.2 6.2 5.2 8 8.8 4" stroke="var(--maroon)" stroke-width="1.6" fill="none"/></svg>Mining Services</li>
    <li><svg viewBox="0 0 12 12"><circle cx="6" cy="6" r="6" fill="#fff"/><path d="M3.2 6.2 5.2 8 8.8 4" stroke="var(--maroon)" stroke-width="1.6" fill="none"/></svg>Facilities Management</li>
  </ul>
  <p class="mission">Committed to growing the economy by<br>contributing to infrastructure development through the provision of<br>world class services in roads &amp; civils, buildings, water &amp; sanitation,<br>structures &amp; property development in<br>South Africa</p>
  <div class="photo services-photo" role="img" aria-label="Single-storey office complex with terracotta roofs and trees under a deep blue sky"></div>
  <div class="page-number" style="left:461px; top:650px; background:var(--maroon);">3</div>
  <footer class="footer">
    <svg width="522" height="58" viewBox="0 0 522 58">
      <rect width="522" height="58" fill="var(--charcoal)"/>
      <polygon points="370,0 522,0 522,58 420,58" fill="var(--white)"/>
    </svg>
    <p class="footer-tag">INFRASTRUCTURE<br>PROVIDER OF DISTINCTION</p>
    <p class="footer-url">www.kelmoritaestates.co.za</p>
    <div class="brand footer-brand">KELMORITA<br>ESTATES</div>
  </footer>
</section>

<!-- Contents page -->
<section class="page page--contents">
  <div class="contents-column"></div>
  <h2 class="contents-heading">TABLE OF<strong>CONTENTS</strong></h2>
  <span class="quote-mark quote-open">“</span>
  <p class="contents-quote">Infrastructure<br>Provider of<br>Distinction</p>
  <span class="quote-mark quote-close">”</span>
  <ol class="toc">
    <li><span>Introduction</span><span>05</span></li>
    <li><span>About Us</span><span>06</span></li>
    <li><span>Journey &amp; Accreditation</span><span>07</span></li>
    <li><span>Services</span><span>08</span></li>
    <li><span>Buildings</span><span>09</span></li>
    <li><span>Roads &amp; Civils</span><span>10</span></li>
    <li><span>Property Development</span><span>11</span></li>
    <li><span>Mining Services &amp; Infrastructure</span><span>12</span></li>
    <li><span>Facilities Management</span><span>13</span></li>
    <li><span>Feature Projects</span><span>16</span></li>
    <li><span>Core Capabilities</span><span>14</span></li>
    <li><span>Corporate Social Responsibility</span><span>26</span></li>
  </ol>
  <div class="photo contents-photo" role="img" aria-label="Front view of a modern multi-storey building with grey cladding and red columns"></div>
  <footer class="footer">
    <svg width="522" height="58" viewBox="0 0 522 58">
      <rect width="522" height="58" fill="var(--charcoal)"/>
      <polygon points="370,0 522,0 522,58 420,58" fill="var(--white)"/>
    </svg>
    <p class="footer-tag">INFRASTRUCTURE<br>PROVIDER OF DISTINCTION</p>
    <p class="footer-url">www.kelmoritaestates.co.za</p>
    <div class="brand footer-brand">KELMORITA<br>ESTATES</div>
  </footer>
</section>

</body>
</html>
```